Tal Moran needs a label design

Tal Moran specializes in Professional Solutions for skin problems

We need a tube design for professional cosmetics skin problems.
It should show that it is cosmetics but more pharma. The product is a professional treat cosmetics like medicine (but not medicine).

See sample of our tubes in our site: www.talmoran.example
The new tubes will be shorter.

The size of the tube is approximately 100mm high and 40mm front (when you are looking on the front of the tube.

I want a clean look, can be traditional but with modern look.
Will be one of a line, changing by color on each one in the line.

In the line:
Sun Hazard protection.
Calming from Psoriasis.
Treatment fot Savorea.
Very dry skin.
Skin firming serum.
Very dry diabetic foot.

Target Market(s)

pharmacies

Industry/Entity Type

Pharmacy

Font styles to use
Serif

Colors
0255a3

Requirements
Must have
• how to use
Nice to have
• specification of ingredients

```html
<!DOCTYPE html>
<html lang="en">
<head>
<meta charset="utf-8">
<title>Tal Moran – Professional Skin Line Label</title>
<link rel="stylesheet" href="https://fonts.googleapis.com/css2?family=Open+Sans:wght@700&display=swap">
<style>
  :root {
    --blue-top: #1f74f6;
    --blue-mid: #1657d6;
    --blue-deep: #0a379a;
    --strip-light: #3a9cff;
    --band-sun: #2a6cf0;
    --band-calm: #1c5be2;
    --ink-white: #ffffff;
    --ink-cyan: #36e2ec;
    --ink-yellow: #f2f21e;
    --ink-sky: #4fd6ff;
    --ink-red: #ff1c1c;
    --ink-green: #25ff25;
  }
  * { margin: 0; padding: 0; box-sizing: border-box; }
  html, body {
    width: 1200px;
    height: 3000px;
    overflow: hidden;
    background: var(--blue-deep);
  }
  .label {
    position: relative;
    width: 1200px;
    height: 3000px;
    overflow: hidden;
    font-family: "Open Sans", Arial, sans-serif;
    font-weight: 700;
    background: linear-gradient(180deg, var(--blue-top) 0%, var(--blue-mid) 45%, var(--blue-deep) 100%);
  }
  .brand-name {
    position: absolute;
    top: 419px;
    left: 0;
    width: 1100px;
    text-align: center;
    font-size: 180px;
    line-height: 200px;
    color: var(--ink-white);
    letter-spacing: -1px;
    white-space: nowrap;
  }
  .strip {
    position: absolute;
    left: 0;
    width: 100%;
    background: var(--strip-light);
  }
  .strip--top { top: 0; height: 32px; }
  .strip--upper { top: 700px; height: 60px; }
  .strip--lower { top: 1112px; height: 40px; }
  .band {
    position: absolute;
    left: 0;
    width: 100%;
  }
  .band--sun { top: 760px; height: 352px; background: var(--band-sun); }
  .band--calm { top: 1152px; height: 328px; background: var(--band-calm); }
  .line-item {
    position: absolute;
    left: 224px;
    font-size: 99px;
    line-height: 116px;
    letter-spacing: -0.5px;
    white-space: nowrap;
  }
  .line-item--sun { top: 802px; color: var(--ink-white); }
  .line-item--psoriasis { top: 1182px; color: var(--ink-cyan); }
  .line-item--seborrhea { top: 1566px; color: var(--ink-yellow); }
  .line-item--dry-skin { top: 1934px; color: var(--ink-sky); }
  .line-item--firming { top: 2202px; color: var(--ink-red); }
  .line-item--diabetic { top: 2574px; color: var(--ink-green); }
  .line-item .indent { padding-left: 18px; }
</style>
</head>
<body>
  <main class="label">
    <div class="strip strip--top"></div>
    <div class="brand-name">Tal Moran</div>

    <div class="strip strip--upper"></div>
    <div class="band band--sun"></div>
    <div class="strip strip--lower"></div>
    <div class="band band--calm"></div>

    <p class="line-item line-item--sun">Sun Hazard<br>protection.</p>
    <p class="line-item line-item--psoriasis">Calming from<br>Psoriasis.</p>
    <p class="line-item line-item--seborrhea">Treatment fot<br>Savorea.</p>
    <p class="line-item line-item--dry-skin">Very dry skin.</p>
    <p class="line-item line-item--firming">Skin firming<br>serum.</p>
    <p class="line-item line-item--diabetic">Very dry diabetic<br><span class="indent">foot.</span></p>
  </main>
</body>
</html>
```